Software Company Requires Website

We need a web design for a new mobile software development company based in London named Velmark Solutions.
The design needs to be clean and smooth. Not too flashy, not too boring.
I would like to try the design with some warm colors, and maybe a headline or something highlighted with a strong color. ( logo ? ) The layout should be something like the bellow links, all in one page.

http://quorbit.example/
http://www.telvane.example/
http://www.work-plover.example/
http://www.brisk.example/
http://www.fenlowtech.example/us/

Now some of them they seem different from the others, but in each of them there is something that ticks my brain, so it`s up to you to surprise me.

I have uploaded the logo of the company, so you guys can fit that in your design as well.
Updates

Hy everybody This will be the last update for the brief. The company will focus in the beginning for mobile development only, so i would like the website design to be done in a matter that will reflect that. We will develop IOS, Android and Windows applications. We will also require 3 pages: One for the home menu, one for portfolio and one for contact us. The layout should be the same ( one page scroll down ) but the design of the 3 pages different. Please readdress the brief. Hope that i provided enough information for the scope of the project.

I have uploaded the logo that you guys can use. If the logo requires small modifications you can adjust that to suit your idea as long as the logo does not change completely.

Target Market(s)

High End companies that require simplified software solutions.

Industry/Entity Type

It Company

Number of Pages Required

3 page

Requirements
Must have
• One page scroll down layout for 3 pages:
• one for home page, one for portfolio and one for contact us.
• In the portfolio page we would like to have different display options for given examples of applications ( min 3 )

```html
<!DOCTYPE html>
<html lang="en">
<head>
<meta charset="utf-8">
<title>Velmark Solutions – Mobile Software Development</title>
<link href="https://fonts.googleapis.com/css2?family=Oswald:wght@300;500&family=Open+Sans:ital,wght@0,400;0,600;0,700;1,400&display=swap" rel="stylesheet">
<style>
:root{
  --blue:#2b7cc9;
  --blue-dark:#1c62a8;
  --blue-band:#2f7fc6;
  --ink:#2c2c2c;
  --text:#555;
  --muted:#8a8a8a;
  --light:#f1f1f1;
  --white:#fff;
  --night:#1b2a3a;
  --line:#dcdcdc;
}
*{box-sizing:border-box;margin:0;padding:0}
html,body{width:1200px;height:3013px;overflow:hidden}
body{font-family:"Open Sans",Arial,sans-serif;color:var(--text);background:var(--white);position:relative}
section,header,footer{position:absolute;left:0;width:1200px}
.abs{position:absolute}
.section-title{position:absolute;left:0;width:1200px;text-align:center;font-size:29px;font-weight:600;color:var(--ink)}
.section-title span{color:var(--blue)}
.section-title::after{content:"";display:block;width:150px;height:1px;background:var(--line);margin:10px auto 0}
.btn-small{position:absolute;height:28px;padding:0 36px 0 14px;background:var(--blue-dark);color:var(--white);font-size:13px;font-weight:700;line-height:28px;border-radius:2px}
.btn-small::after{content:"›";position:absolute;right:6px;top:4px;width:20px;height:20px;border-radius:50%;background:var(--white);color:var(--blue);line-height:19px;text-align:center;font-size:16px}

/* header */
.site-header{top:0;height:95px;background:var(--white)}
.brand-band{position:absolute;left:0;top:0}
.brand{position:absolute;left:133px;top:22px;display:flex;align-items:center;gap:12px;color:var(--white);font-size:27px;font-weight:700}
.brand i{display:block;width:40px;height:40px;border:3px solid var(--white)}
.top-icons{position:absolute;right:135px;top:8px;display:flex;gap:12px}
.top-icons b{width:28px;height:22px;background:var(--blue);border-radius:3px;display:block}
.nav{position:absolute;right:135px;top:58px;display:flex;gap:48px;font-size:15px;color:var(--ink)}
.nav .active{color:var(--blue);border-bottom:3px solid var(--blue);padding:0 14px 8px}

/* hero */
.hero{top:95px;height:540px}
.hero-photo{position:absolute;inset:0;background:linear-gradient(90deg,#4e5c6c 0%,#6d7c8c 45%,#3b4654 100%)}
.hero-title{position:absolute;left:133px;top:142px;color:var(--white);font-family:"Oswald",sans-serif}
.hero-title h1{font-size:44px;font-weight:500;line-height:1.1}
.hero-title p{font-size:29px;font-weight:300;letter-spacing:.5px}
.platforms{position:absolute;left:133px;top:268px;display:flex;gap:15px}
.platforms b{width:56px;height:56px;background:#e9ecef;border-radius:3px;display:block}
.learn-more{position:absolute;left:133px;top:358px;width:148px;height:42px;background:var(--blue);color:var(--white);font-size:16px;line-height:42px;padding-left:14px;border-radius:2px}
.learn-more::after{content:"›";position:absolute;right:12px;top:11px;width:20px;height:20px;border:1.5px solid var(--white);border-radius:50%;text-align:center;line-height:17px}

/* welcome */
.welcome{top:635px;height:281px}
.welcome h2{position:absolute;top:28px;width:1200px;text-align:center;font-size:27px;font-weight:400;color:var(--ink)}
.welcome h2 b{color:var(--blue-dark);font-weight:700}
.lead{position:absolute;left:133px;width:934px;top:90px;text-align:center;color:var(--blue);font-size:14.5px;line-height:24px}
.body-copy{position:absolute;left:133px;width:934px;top:158px;text-align:center;font-size:13px;line-height:22px}

/* services */
.services{top:916px;height:407px;background:var(--light)}
.service{position:absolute;top:105px;width:300px;text-align:center}
.service .icon{width:113px;height:113px;border-radius:50%;background:var(--blue);margin:0 auto;border:5px solid #d6e4f2;display:flex;align-items:center;justify-content:center}
.service h3{font-size:16px;color:var(--ink);margin-top:24px;font-weight:700}
.service p{font-size:13px;line-height:19px;margin-top:12px;padding:0 25px}
.service a{display:block;color:var(--blue);font-size:13px;margin-top:16px}

/* solution */
.solution{top:1323px;height:427px}
.solution-text{position:absolute;left:133px;top:102px;width:470px}
.solution-text h3{font-size:18px;font-weight:700;color:var(--ink)}
.solution-text h3 span{color:var(--blue);font-weight:400}
.solution-text .sub{font-size:13px;margin-top:6px}
.ticks{list-style:none;margin-top:12px}
.ticks li{font-size:13px;line-height:28px;padding-left:24px;position:relative}
.ticks li::before{content:"";position:absolute;left:2px;top:9px;width:9px;height:5px;border-left:2px solid var(--blue);border-bottom:2px solid var(--blue);transform:rotate(-45deg)}
.laptop{position:absolute;left:602px;top:108px;width:465px;height:282px;background:linear-gradient(180deg,#2a2a2e 0%,#1a3a6a 50%,#c9c9c9 96%);border-radius:8px}

/* works */
.works{top:1750px;height:313px;background:var(--light)}
.work{position:absolute;top:107px;width:289px;height:166px}

/* testimonials */
.testimonials{top:2063px;height:289px;background:var(--blue-band)}
.testimonials .section-title{color:var(--white)}
.testimonials .section-title::after{background:rgba(255,255,255,.4)}
.quote{position:absolute;top:110px;width:420px}
.avatar{position:absolute;left:0;top:8px;width:95px;height:95px;border-radius:50%;border:4px solid var(--white)}
.quote p{position:absolute;left:125px;width:300px;color:var(--white);font-style:italic;font-size:13px;line-height:19px;text-align:right}
.quote p::before{content:"“";position:absolute;left:0;top:-10px;font-size:40px;font-style:normal;opacity:.7}
.quote .name{position:absolute;left:140px;top:122px;color:var(--white);font-size:13px;width:260px;text-align:center}
.dots{position:absolute;left:0;width:1200px;top:270px;display:flex;justify-content:center;gap:6px}
.dots b{width:10px;height:10px;border-radius:50%;border:1.5px solid var(--blue-dark);background:var(--white)}
.dots b:first-child{background:var(--blue-dark)}

/* partners */
.partners{top:2352px;height:158px;background:var(--white)}
.partner-row{position:absolute;left:133px;width:934px;top:100px;display:flex;justify-content:space-between;align-items:center}
.partner{display:flex;align-items:center;gap:8px;font-size:24px;font-weight:600;color:#3a3a3a}
.partner i{width:20px;height:20px;border:2px solid #3a3a3a;border-radius:50%}

/* contact */
.contact{top:2510px;height:452px;background:linear-gradient(180deg,#2c3d4f 0%,#1d2c3b 60%,#16222e 100%)}
.contact .section-title{color:var(--white);top:30px}
.contact .section-title::after{display:none}
.contact h4{position:absolute;font-size:22px;font-weight:600;color:#4a9be0}
.field{position:absolute;left:133px;width:449px;height:38px;border:1px solid rgba(255,255,255,.25);background:rgba(255,255,255,.04);color:var(--white);font-size:12px;padding:10px 12px}
.submit{position:absolute;left:133px;top:392px;width:95px;height:38px;background:var(--blue);color:var(--white);font-size:14px;font-weight:600;text-align:center;line-height:38px}
.detail{position:absolute;left:715px;display:flex;gap:16px;color:#d9e1e8;font-size:13px;line-height:19px;width:400px}
.detail svg{flex:none}
.social{position:absolute;left:715px;top:392px;display:flex;gap:8px}
.social b{width:28px;height:28px;border-radius:50%;background:var(--white)}

.site-footer{top:2962px;height:51px;background:#f2f2f2;text-align:center;font-size:12px;line-height:51px;color:#555}
</style>
</head>
<body>

<header class="site-header">
  <svg class="brand-band" width="430" height="95" viewBox="0 0 430 95"><polygon points="0,0 395,0 430,47 395,95 0,95" fill="#2b7cc9"/></svg>
  <div class="brand"><i></i>Velmark Solutions</div>
  <div class="top-icons"><b></b><b></b><b></b></div>
  <nav class="nav"><span class="active">Home</span><span>Portfolio</span><span>Contact Us</span></nav>
</header>

<section class="hero">
  <div class="hero-photo" role="img" aria-label="Businessman in a suit touching a glowing cloud icon surrounded by a network of app icons"></div>
  <div class="hero-title"><h1>MOBILE SOFTWARE</h1><p>DEVELOPMENT COMPANY</p></div>
  <div class="platforms"><b></b><b></b><b></b></div>
  <div class="learn-more">Learn More</div>
  <svg class="abs" style="left:80px;top:245px" width="20" height="40"><polyline points="18,2 2,20 18,38" fill="none" stroke="#ffffff" stroke-opacity=".5" stroke-width="2"/></svg>
  <svg class="abs" style="left:1100px;top:245px" width="20" height="40"><polyline points="2,2 18,20 2,38" fill="none" stroke="#ffffff" stroke-opacity=".5" stroke-width="2"/></svg>
  <svg class="abs" style="left:582px;top:490px" width="36" height="30"><polyline points="3,4 18,16 33,4" fill="none" stroke="#fff" stroke-width="4"/><polyline points="3,14 18,26 33,14" fill="none" stroke="#fff" stroke-width="4"/></svg>
</section>

<section class="welcome">
  <h2>Welcome to <b>Velmark</b></h2>
  <p class="lead">Ut wisi enim ad minim veniam, quis nostrud exerci tation ullamcorper suscipit lobortis nisl ut aliquip ex ea commodo dignissim qui blandit adipiscing consequat.</p>
  <p class="body-copy">Duis autem vel eum iriure dolor in hendrerit in vulputate velit esse molestie consequat, vel illum dolore eu feugiat nulla facilisis at vero eros et accumsan et iusto odio dignissim qui blandit praesent luptatum zzril delenit augue duis dolore te feugait nulla facilisi.</p>
  <div class="btn-small" style="left:540px;top:216px">Read more</div>
</section>

<section class="services">
  <h2 class="section-title" style="top:30px">Our <span>Services</span></h2>
  <div class="service" style="left:116px">
    <div class="icon"><svg width="44" height="60"><rect x="6" y="2" width="32" height="56" rx="5" fill="none" stroke="#fff" stroke-width="3"/><rect x="11" y="10" width="22" height="36" fill="#fff"/></svg></div>
    <h3>Mobile App Development</h3>
    <p>Ut wisi enim ad minim veniam, quisosm nostrud exerci tation ullamcorper mor suscipit lobortis nisl onsequat.</p>
    <a>Read More »</a>
  </div>
  <div class="service" style="left:447px">
    <div class="icon"><svg width="64" height="44"><rect x="4" y="6" width="56" height="32" rx="16" fill="#fff"/><rect x="13" y="19" width="14" height="4" fill="#2b7cc9"/><rect x="18" y="14" width="4" height="14" fill="#2b7cc9"/><circle cx="44" cy="17" r="3" fill="#2b7cc9"/><circle cx="50" cy="24" r="3" fill="#2b7cc9"/></svg></div>
    <h3>Mobile Game Development</h3>
    <p>Ut wisi enim ad minim veniam, quisosm nostrud exerci tation ullamcorper mor suscipit lobortis nisl onsequat.</p>
    <a>Read More »</a>
  </div>
  <div class="service" style="left:781px">
    <div class="icon"><svg width="64" height="54"><path d="M14 30 a10 10 0 0 1 4-19 a14 14 0 0 1 26 2 a9 9 0 0 1 6 17 z" fill="#fff"/><path d="M32 30 v10 M18 44 h28 M18 40 v8 M32 40 v8 M46 40 v8" stroke="#fff" stroke-width="3" fill="none"/></svg></div>
    <h3>Mobile Cloud Computing</h3>
    <p>Ut wisi enim ad minim veniam, quisosm nostrud exerci tation ullamcorper mor suscipit lobortis nisl onsequat.</p>
    <a>Read More »</a>
  </div>
</section>

<section class="solution">
  <h2 class="section-title" style="top:30px">Our <span>Solution</span></h2>
  <div class="solution-text">
    <h3>A progressive <span>Mobile software development company!</span></h3>
    <p class="sub">Other Services we are offering</p>
    <ul class="ticks">
      <li>Ut wisi enim ad minim veniam, quisosm</li>
      <li>Quisosm nostrud exerci tation ullamcorper mor</li>
      <li>Ullamcorper mor suscipit lobortis nisl onsequat</li>
      <li>Duis autem vel eum iriure dolor</li>
      <li>Commodo dignissim qui blandit adipiscing</li>
      <li>Feugiat nulla facilisis at vero eros</li>
    </ul>
  </div>
  <div class="btn-small" style="left:133px;top:364px">Read more</div>
  <div class="laptop" role="img" aria-label="Laptop showing a smartphone with colourful app icons bursting from its screen"></div>
</section>

<section class="works">
  <h2 class="section-title" style="top:28px">View <span>Our Works</span></h2>
  <div class="work" style="left:133px;background:linear-gradient(180deg,#2a2a2a 0%,#3a3a3a 55%,#e9b92e 56%,#f0c23a 100%)" role="img" aria-label="App project shown on phones over a dark and yellow backdrop"></div>
  <div class="work" style="left:454px;background:linear-gradient(135deg,#cfe6f6 0%,#8fc4ea 50%,#e7f2fb 100%)" role="img" aria-label="Hands holding a phone with a colourful game app"></div>
  <div class="work" style="left:778px;background:linear-gradient(135deg,#2f4a6e 0%,#3c5c86 60%,#2a4262 100%)" role="img" aria-label="Medical app project tile"></div>
</section>

<section class="testimonials">
  <h2 class="section-title" style="top:30px">Our Client Says</h2>
  <div class="quote" style="left:133px">
    <div class="avatar" style="background:#c9b4a0" role="img" aria-label="Client portrait"></div>
    <p>Lorem ipsum dolor sit amet, consectetuer adipiscing elit, sed diam nonummy nibh euismod tincidunt ut laoreet dolore magna aliquam erat volutpat.</p>
    <div class="name">Mr. Mark Halden</div>
  </div>
  <div class="quote" style="left:630px">
    <div class="avatar" style="background:#d9bb8e" role="img" aria-label="Client portrait"></div>
    <p>Lorem ipsum dolor sit amet, consectetuer adipiscing elit, sed diam nonummy nibh euismod tincidunt ut laoreet dolore magna aliquam erat volutpat.</p>
    <div class="name">Miss Nora Pell</div>
  </div>
  <div class="dots"><b></b><b></b><b></b><b></b></div>
</section>

<section class="partners">
  <h2 class="section-title" style="top:22px">Our <span>Partners</span></h2>
  <div class="partner-row">
    <div class="partner">Arlow</div>
    <div class="partner"><i></i>Corveth</div>
    <div class="partner"><i></i>Tinmoor</div>
    <div class="partner">Pallisade</div>
    <div class="partner"><i></i>Quenby</div>
  </div>
</section>

<section class="contact" role="img" aria-label="Dusky city street scene behind the contact area">
  <h2 class="section-title">Get In Touch</h2>
  <h4 style="left:133px;top:100px">Drop us a line</h4>
  <div class="field" style="top:146px">Name</div>
  <div class="field" style="top:193px">Email</div>
  <div class="field" style="top:238px">Phone</div>
  <div class="field" style="top:281px;height:84px">Message</div>
  <div class="submit">SUBMIT</div>

  <h4 style="left:715px;top:100px">Contact Details</h4>
  <div class="detail" style="top:158px"><svg width="14" height="20"><path d="M7 0a7 7 0 0 1 7 7c0 5-7 13-7 13S0 12 0 7a7 7 0 0 1 7-7z" fill="#4a9be0"/><circle cx="7" cy="7" r="2.5" fill="#1d2c3b"/></svg><span>Lorem ipsum dolor sit amet, consectetuer adipi scing elit, sed diam nonummy nibh euismod tincidunt ut laore</span></div>
  <div class="detail" style="top:222px"><svg width="14" height="16"><path d="M3 1l3 3-2 2a8 8 0 0 0 5 5l2-2 3 3-2 3C6 15 0 9 0 3z" fill="#4a9be0"/></svg><span>+123 456 7890</span></div>
  <div class="detail" style="top:260px"><svg width="14" height="12"><rect x="0" y="1" width="14" height="10" fill="#4a9be0"/><polyline points="0,1 7,7 14,1" fill="none" stroke="#1d2c3b" stroke-width="1.5"/></svg><span>info@velmarksolutions.example</span></div>
  <h4 style="left:715px;top:332px">Follow us</h4>
  <div class="social"><b></b><b></b><b></b><b></b></div>
</section>

<footer class="site-footer">© 2014 Velmark Solutions. All rights reserved.</footer>

</body>
</html>
```